Simple elegant business card

General card for a fin and television director.
Just want name, email, phone and address.

Target Market(s)

Prospective employers

Industry/Entity Type

Business

Requirements
Must have
• As above
Nice to have
• Logo but not necessary.
Should not have
• Not too colourful or funky.
• Simplicity and elegance the way to go.

```html
<!DOCTYPE html>
<html lang="en">
<head>
<meta charset="utf-8">
<title>Nora Hale – Business Card</title>
<link rel="stylesheet" href="https://fonts.googleapis.com/css2?family=Open+Sans:wght@700&family=Tinos:ital,wght@0,400;1,400&display=swap">
<style>
  :root {
    --stage: #0c1f12;
    --card-black: #000000;
    --card-white: #ffffff;
    --ink: #111111;
    --role-blue: #2a2ad0;
    --mark-lavender: #b9b6ff;
    --back-deep: #c24a4a;
    --back-light: #fbe9e9;
    --back-text: #6a6a6a;
    --edge: #000000;
  }
  * { margin: 0; padding: 0; box-sizing: border-box; }
  html, body { width: 1200px; height: 960px; overflow: hidden; }
  body { background: var(--stage); position: relative; font-family: "Tinos", serif; }

  .card { position: absolute; width: 520px; height: 300px; }

  .card-front { left: 190px; top: 140px; background: var(--card-black); }
  .card-front svg.panel { position: absolute; inset: 0; }
  .brand {
    position: absolute; left: 22px; top: 200px; width: 150px;
    display: flex; flex-direction: column; align-items: center; gap: 8px;
  }
  .brand-dot { width: 44px; height: 44px; border-radius: 50%; background: var(--mark-lavender); }
  .brand-name { font-family: "Tinos", serif; font-size: 19px; color: var(--mark-lavender); letter-spacing: 1px; }

  .identity { position: absolute; left: 250px; top: 44px; width: 250px; text-align: center; }
  .identity-name { font-family: "Open Sans", sans-serif; font-weight: 700; font-size: 24px; color: var(--ink); }
  .identity-role { font-family: "Tinos", serif; font-style: italic; font-size: 20px; color: var(--role-blue); }

  .contact { position: absolute; left: 212px; top: 178px; font-family: "Tinos", serif; font-size: 20px; color: var(--ink); line-height: 1.25; }
  .contact span { display: inline-block; width: 78px; }

  .card-back {
    left: 470px; top: 470px;
    border: 4px solid var(--edge);
    background: radial-gradient(ellipse at center, var(--back-light) 0%, #e9a9a9 45%, var(--back-deep) 100%);
    display: flex; align-items: center; justify-content: center;
  }
  .back-name { font-family: "Tinos", serif; font-size: 44px; color: var(--back-text); }
</style>
</head>
<body>
  <section class="card card-front" aria-label="Business card front">
    <svg class="panel" width="520" height="300" viewBox="0 0 520 300" aria-hidden="true">
      <path d="M200 0 H520 V300 H165 V190 C165 150 225 130 225 80 C225 40 205 20 200 0 Z" fill="var(--card-white)" stroke="#3a3ab0" stroke-width="1.5"/>
    </svg>
    <div class="brand">
      <div class="brand-dot"></div>
      <div class="brand-name">NORA HALE</div>
    </div>
    <div class="identity">
      <div class="identity-name">Nora Hale</div>
      <div class="identity-role">Tv Director</div>
    </div>
    <div class="contact">
      <div>Email:norahale@mail.example</div>
      <div><span>Phone:</span>+1 310 555 0142</div>
    </div>
  </section>

  <section class="card card-back" aria-label="Business card back">
    <div class="back-name">Nora Hale</div>
  </section>
</body>
</html>
```